Kelverin Roofing & Restoration Business Card Design

Lookiing for a double sided business card design that will have rounded corners, will look good with Spot UV, Soft Laminate, or Gloss
Front of card should have Logo, Name and Contact Info, License numbers
Back of card should have Logo, maybe other small details

```html
<!DOCTYPE html>
<html lang="en">
<head>
<meta charset="utf-8">
<title>Kelverin Roofing &amp; Restoration – Business Card</title>
<link href="https://fonts.googleapis.com/css2?family=Poppins:wght@400;600&family=Arimo:wght@400&display=swap" rel="stylesheet">
<style>
  :root{
    --page:#e6e6e6;
    --charcoal-top:#464646;
    --charcoal:#333333;
    --brand-blue:#00b2e6;
    --brand-blue-deep:#00a9e0;
    --white:#ffffff;
    --rule:#6a6a6a;
  }
  html,body{margin:0;padding:0;width:1200px;height:1200px;overflow:hidden;background:var(--page);}
  .stage{position:relative;width:1400px;height:1400px;transform:scale(0.857143);transform-origin:0 0;}
  .card{position:absolute;width:803px;height:459px;border-radius:6px;overflow:hidden;}
  .card--front{left:299px;top:185px;background:linear-gradient(180deg,var(--charcoal-top) 0%,var(--charcoal) 80%);}
  .card--back{left:299px;top:762px;background:linear-gradient(180deg,var(--brand-blue) 0%,var(--brand-blue-deep) 100%);}

  .wordmark{position:absolute;font-family:"Poppins",sans-serif;font-weight:600;color:var(--white);text-transform:uppercase;line-height:1.2;}
  .card--front .wordmark{right:403px;top:153px;font-size:23px;text-align:right;}
  .card--back .wordmark{left:0;right:0;top:178px;font-size:42px;text-align:center;}

  .divider{position:absolute;left:434px;top:72px;width:2px;height:248px;background:var(--rule);}

  .contact{position:absolute;left:460px;top:70px;font-family:"Arimo",sans-serif;color:var(--white);}
  .contact__name{margin:0;font-family:"Poppins",sans-serif;font-weight:600;font-size:30px;line-height:40px;color:var(--brand-blue);}
  .contact__role{margin:0 0 18px;font-family:"Poppins",sans-serif;font-size:17px;line-height:20px;}
  .contact__address{margin:0 0 12px;font-size:19px;line-height:25px;font-style:normal;}
  .contact__list{list-style:none;margin:0 0 12px;padding:0;font-size:19px;line-height:24px;}
  .contact__list li{display:flex;align-items:center;gap:14px;}
  .contact__list svg{width:16px;height:16px;fill:var(--brand-blue);flex:none;}
  .contact__licence{margin:0;font-size:19px;line-height:24px;}

  .footer-band{position:absolute;left:0;top:378px;width:626px;height:40px;background:var(--brand-blue);}
  .footer-band__url{position:absolute;left:104px;top:9px;font-family:"Arimo",sans-serif;font-size:19px;color:var(--white);}
  .footer-mark{position:absolute;left:630px;top:378px;width:46px;height:40px;display:flex;align-items:center;justify-content:center;}
  .footer-mark span{width:18px;height:18px;background:var(--white);}
  .footer-tab{position:absolute;left:676px;top:378px;width:127px;height:40px;background:var(--white);}
</style>
</head>
<body>
<main class="stage">
  <section class="card card--front" aria-label="Card front">
    <div class="wordmark">Kelverin Roofing &amp;<br>Restoration</div>
    <div class="divider"></div>
    <div class="contact">
      <h1 class="contact__name">DORIAN HALE</h1>
      <p class="contact__role">President</p>
      <address class="contact__address">412 Alder Crest Road<br>Fairbrook, Canada 58210</address>
      <ul class="contact__list">
        <li><svg viewBox="0 0 16 16" aria-hidden="true"><path d="M3.5 1l3 3-1.6 2c.9 2 2.5 3.6 4.5 4.5l2-1.6 3 3-2 2.1C7.5 13.5 2.5 8.5 1.4 3z"/></svg>555-214-7730</li>
        <li><svg viewBox="0 0 16 16" aria-hidden="true"><path d="M4 0h8v16H4zM5.5 1.5v11h5v-11z"/></svg>555-214-7791</li>
        <li><svg viewBox="0 0 16 16" aria-hidden="true"><path d="M1 3h14v10H1zM2.5 4.5L8 9l5.5-4.5z"/></svg>info@kelverin.com</li>
      </ul>
      <p class="contact__licence">LIC.NO 4816</p>
    </div>
    <div class="footer-band"><span class="footer-band__url">www.kelverin.com</span></div>
    <div class="footer-mark"><span></span></div>
    <div class="footer-tab"></div>
  </section>

  <section class="card card--back" aria-label="Card back">
    <div class="wordmark">Kelverin Roofing &amp;<br>Restoration</div>
  </section>
</main>
</body>
</html>
```